We need a flyer where we promote a workshop to our members of the jewish community www.qvb-gemeinde.example . The workshop is calles "guidance in ten seasons presented by QVB. We would like to see a flyer with the below text is used and also some pictures (attached). The flyer should come over as cool, fresh, innovative for a younger crowd so called young professionals (age 28-35).
TITLE.
"Guidance in Ten Seasons.
SUBTITLE.
Your systematic self-coaching roadmap to power and impact—and your future.”
TEXT.
Dr. Martin K. Halvorsen is the CEO Emeritus of Alpine Advisory Partners—he made an exit in 2013. He is the award-winning author of 8 books, including "Plan-Into-Motion," "Speak or Falter" and "The Cantor and the Chairman.”
For the past 20 years he has taught leadership at Harwick University in New York and at BKU (Lindenberg University) to prepare future CEOs and other leaders in business, government , nonprofits and the military.
Now, in a process exclusively designed for QVB’s next generation of emerging leaders, Martin unpacks his leadership secrets in 3 action-packed labs—reduced to the max:
Lab 1. Guidance in Ten Seasons: The Summit Guide Triangle®. Self-Assessment. Self-Leadership: “The Lantern.” 5-Year Vision. 100-Day Catalytic Project.
Lab 2. Leading Through Language. Relationship: Building Trust. Plan-Into-Motion. Cockpit.
Lab 3. Debrief and Scale-Up. Sustainability. Action Tools.
Do you want to build your own future and a life you love? Do you want to jump-start that future and life over 100 days while learning a toolbox of leadership skills, networking with like-minded people—and even get some pizza? Then join us.
Target Market(s)
young professionals age 28-35

```html
<!DOCTYPE html>
<html lang="en">
<head>
<meta charset="utf-8">
<title>Guidance in Ten Seasons – Workshop Flyer</title>
<link rel="stylesheet" href="https://fonts.googleapis.com/css2?family=Anton&family=Oswald:wght@500;600&family=Roboto:ital,wght@0,400;0,500;0,700;1,700&display=swap">
<style>
  :root {
    --navy: #123a6c;
    --navy-deep: #0f2f6e;
    --teal: #2196c4;
    --teal-band: #2190c0;
    --slate: #2f3a4e;
    --slate-light: #5d6b86;
    --mist: #e2ecec;
    --lab-tag: #6aa5bd;
    --lab-row: #e1ebf4;
    --ink: #1c1c22;
    --body-blue: #1f3f7a;
    --footer-light: #a9cfe0;
    --white: #ffffff;
  }
  * { box-sizing: border-box; margin: 0; padding: 0; }
  html, body { width: 848px; height: 1200px; overflow: hidden; background: var(--white); }
  .flyer { position: relative; width: 848px; height: 1200px; overflow: hidden; background: var(--white); font-family: "Roboto", Arial, sans-serif; }

  /* hero */
  .hero { position: absolute; left: 0; top: 0; width: 848px; height: 452px; background: var(--mist); }
  .hero-block { position: absolute; left: 0; top: 0; width: 320px; height: 452px; background: var(--navy-deep); }
  .hero-photo { position: absolute; left: 0; top: 0; width: 848px; height: 452px; }
  .title { position: absolute; left: 405px; top: 28px; width: 430px; font-family: "Anton", Impact, sans-serif; font-weight: 400; line-height: .95; text-transform: uppercase; white-space: nowrap; }
  .title-main { display: block; font-size: 104px; color: var(--navy); letter-spacing: 1px; }
  .title-sub { display: block; font-size: 66px; color: var(--teal); }
  .subtitle { position: absolute; left: 410px; top: 196px; width: 430px; font-weight: 700; font-size: 27px; line-height: 34px; color: #163c78; white-space: nowrap; }
  .subtitle span { display: block; }
  .subtitle span:nth-child(2) { padding-left: 17px; }
  .subtitle span:nth-child(3) { padding-left: 35px; }
  .name-band { position: absolute; left: 0; top: 0; width: 848px; height: 452px; }
  .name-band-text { position: absolute; left: 460px; top: 322px; width: 380px; height: 56px; font-family: "Oswald", sans-serif; font-weight: 500; font-size: 33px; line-height: 56px; color: var(--white); text-align: right; white-space: nowrap; }
  .role { position: absolute; left: 477px; top: 380px; font-size: 33px; font-weight: 500; color: var(--white); line-height: 50px; }

  /* bio */
  .stage-photo { position: absolute; left: 0; top: 462px; width: 340px; height: 253px; }
  .bio-chip { position: absolute; left: 343px; top: 461px; width: 340px; height: 33px; background: linear-gradient(90deg, #3c86b9 0%, #6aa2c9 55%, #e4eef6 100%); clip-path: polygon(10px 0, 100% 0, 100% 100%, 0 100%); }
  .bio-chip span { position: absolute; left: 24px; top: 0; font-weight: 700; font-size: 16px; line-height: 33px; color: var(--white); white-space: nowrap; }
  .bio { position: absolute; left: 236px; top: 506px; width: 586px; height: 210px; font-size: 16px; line-height: 20.6px; color: #2a2d36; text-align: justify; }
  .bio-slant { float: left; width: 115px; height: 210px; shape-outside: polygon(0 0, 105px 0, 6px 100%, 0 100%); }
  .bio p + p { margin-top: 18px; }

  /* labs headline */
  .labs-band { position: absolute; left: 0; top: 724px; width: 848px; height: 53px; background: var(--teal-band); box-shadow: 0 4px 0 #d3e3ef; }
  .labs-band h2 { font-family: "Oswald", sans-serif; font-weight: 500; font-size: 25px; line-height: 53px; color: var(--white); text-align: center; white-space: nowrap; letter-spacing: -0.1px; }

  .lab { position: absolute; left: 29px; width: 661px; height: 61px; }
  .lab-1 { top: 801px; } .lab-2 { top: 876px; } .lab-3 { top: 946px; }
  .lab-tag { position: absolute; left: 0; top: 0; width: 102px; height: 61px; background: var(--lab-tag); clip-path: polygon(0 0, 94px 0, 102px 50%, 94px 100%, 0 100%); font-weight: 700; font-size: 20px; line-height: 61px; color: var(--white); padding-left: 17px; }
  .lab-text { position: absolute; left: 100px; top: 0; width: 561px; height: 61px; background: linear-gradient(90deg, var(--lab-row) 0%, #f2f6fa 100%); clip-path: polygon(0 0, 100% 0, 100% 100%, 0 100%, 8px 50%); display: flex; align-items: center; padding-left: 19px; font-size: 16.4px; line-height: 20.5px; color: var(--body-blue); }

  .book { position: absolute; left: 690px; top: 806px; width: 143px; height: 187px; border-radius: 6px; background: linear-gradient(180deg, #1a1a1a 0%, #b31412 12%, #c9201b 60%, #8e0f0d 100%); box-shadow: 0 8px 10px rgba(0,0,0,.25); }

  .cta { position: absolute; left: 30px; top: 1018px; width: 790px; font-size: 16.4px; line-height: 23px; color: var(--ink); }
  .cta em { font-style: italic; font-weight: 700; color: #1f6fb0; }

  /* footer */
  .footer { position: absolute; left: 0; top: 1096px; width: 848px; height: 104px; }
  .contact { position: absolute; top: 1146px; height: 34px; display: flex; align-items: center; gap: 10px; color: var(--white); font-size: 20px; white-space: nowrap; }
  .contact-web { left: 30px; }
  .contact-phone { left: 370px; }
  .brand { position: absolute; left: 660px; top: 1104px; width: 160px; text-align: center; }
  .brand-name { display: block; font-weight: 700; font-size: 60px; line-height: 66px; color: #1b3a9a; letter-spacing: 2px; }
  .brand-label { display: block; font-size: 16px; color: var(--ink); letter-spacing: .5px; margin-top: 2px; }
</style>
</head>
<body>
<main class="flyer">

  <section class="hero">
    <div class="hero-block"></div>
    <svg class="hero-photo" viewBox="0 0 848 452" role="img" aria-label="Portrait photo of Dr. Martin K. Halvorsen in a suit, arms crossed">
      <defs>
        <linearGradient id="portraitTone" x1="0" y1="0" x2="1" y2="1">
          <stop offset="0" stop-color="#d9ecf5"/>
          <stop offset=".55" stop-color="#8fb2cf"/>
          <stop offset="1" stop-color="#3e5474"/>
        </linearGradient>
      </defs>
      <polygon points="18,17 268,17 460,429 18,429" fill="url(#portraitTone)"/>
    </svg>

    <h1 class="title">
      <span class="title-main">Guidance</span>
      <span class="title-sub">in Ten Seasons</span>
    </h1>
    <p class="subtitle">
      <span>Your systematic self-coaching</span>
      <span>roadmap to power and impact</span>
      <span>and your future.</span>
    </p>

    <svg class="name-band" viewBox="0 0 848 452" aria-hidden="true">
      <polygon points="418,322 848,322 848,378 444,378" fill="#2196c4"/>
      <polygon points="446,378 675,378 694,432 470,432" fill="#2f3a4e"/>
      <polygon points="598,378 640,378 612,432 570,432" fill="#5d6b86"/>
      <polygon points="650,378 678,378 650,432 614,432" fill="#6f7b94"/>
      <polygon points="675,378 694,432 652,432" fill="#2f3a4e"/>
    </svg>
    <div class="name-band-text">DR. MARTIN K. HALVORSEN</div>
    <div class="role">CEO</div>
  </section>

  <svg class="stage-photo" viewBox="0 0 340 253" role="img" aria-label="Photo of Dr. Halvorsen speaking on a conference stage in front of an audience">
    <defs>
      <linearGradient id="stageTone" x1="0" y1="0" x2="0" y2="1">
        <stop offset="0" stop-color="#2a2230"/>
        <stop offset=".5" stop-color="#3a2a4a"/>
        <stop offset="1" stop-color="#1d3f8a"/>
      </linearGradient>
    </defs>
    <polygon points="0,0 331,0 216,253 0,253" fill="url(#stageTone)"/>
  </svg>

  <div class="bio-chip"><span>DR. MARTIN K. HALVORSEN</span></div>
  <div class="bio">
    <div class="bio-slant"></div>
    <p>is the CEO Emeritus of Alpine Advisory Partners—he made an exit in 2013. He is the award-winning author of 8 books, including "Plan-Into-Motion," "Speak or Falter" and "The Cantor and the Chairman." For the past 20 years he has taught leadership at Harwick University in New York and at BKU (Lindenberg University) to prepare future CEOs and other leaders in business, government, nonprofits and the military.</p>
    <p>Now, in a process exclusively designed for QVB’s next generation of emerging leaders.</p>
  </div>

  <div class="labs-band"><h2>Martin unpacks his leadership secrets in 3 action-packed labs—reduced to the max:</h2></div>

  <div class="lab lab-1">
    <div class="lab-tag">LAB 1</div>
    <div class="lab-text">Guidance in Ten Seasons: The Summit Guide Triangle®. Self-Assessment. Self-Leadership: “The Lantern.” 5-Year Vision. 100-Day Catalytic Project.</div>
  </div>
  <div class="lab lab-2">
    <div class="lab-tag">LAB 2</div>
    <div class="lab-text">Leading Through Language. Relationship: Building Trust.<br>Plan-Into-Motion. Cockpit.</div>
  </div>
  <div class="lab lab-3">
    <div class="lab-tag">LAB 3</div>
    <div class="lab-text">Debrief and Scale-Up. Sustainability. Action Tools.</div>
  </div>

  <div class="book" role="img" aria-label="Book cover of Guidance in Ten Seasons by Dr. Martin K. Halvorsen"></div>

  <p class="cta">Do you want to build your own future and a life you love? Do you want to jump-start that future and life over 100 days while learning a toolbox of leadership skills, networking with like-minded people—<br>and even get some pizza? <em>THEN JOIN US.</em></p>

  <svg class="footer" viewBox="0 0 848 104" aria-hidden="true">
    <polygon points="640,0 848,0 848,104 584,104" fill="#a9cfe0"/>
    <polygon points="0,22 622,22 583,104 0,104" fill="#2196c4"/>
  </svg>

  <div class="contact contact-web">
    <svg width="30" height="30" viewBox="0 0 32 32" aria-hidden="true" fill="none" stroke="#fff" stroke-width="2.4">
      <circle cx="16" cy="16" r="14"/>
      <ellipse cx="16" cy="16" rx="6" ry="14"/>
      <line x1="2" y1="16" x2="30" y2="16"/>
      <line x1="4.5" y1="9" x2="27.5" y2="9"/>
      <line x1="4.5" y1="23" x2="27.5" y2="23"/>
    </svg>
    <span>www.qvb-gemeinde.example</span>
  </div>
  <div class="contact contact-phone">
    <svg width="20" height="32" viewBox="0 0 22 34" aria-hidden="true" fill="none" stroke="#fff" stroke-width="2.6">
      <rect x="2" y="2" width="18" height="30" rx="3"/>
      <line x1="2" y1="25" x2="20" y2="25"/>
      <circle cx="11" cy="28.5" r="1" fill="#fff"/>
    </svg>
    <span>+41 44 000 12 34</span>
  </div>

  <div class="brand">
    <span class="brand-name">QVB</span>
    <span class="brand-label">PRESENTED BY</span>
  </div>

</main>
</body>
</html>
```